Weight loss surgery restaurant card

We need to create a card for patients who have undergone weight loss surgery to take to restaurants so they can request smaller meals. These patients have had surgery on their stomach so that they can only consume half to one cup of food at a time. So normal sized restaurant meals are way too big (and cost a lot). This card they can present to the restaurant to communicate the fact that they have had weight loss surgery and therefore request a smaller meal portion at reduced cost

Target Market(s)

Restaurants serving weight loss surgery patients

Industry/Entity Type

Health Care

Contact Information for Business Card

This will be a plastic card similar to business card size.

Requirements
Must have
• The front of the card should include the following text:
• The individual bearing this card has undergone weight loss surgery.
• This surgery restricts portion sizes to between half and one cup of food at a time.
• Please give consideration to allowing smaller portions of your regular meals to be ordered to reduce wastage and excess costs.
• Example: a half size portion priced at two thirds of usual cost.
• The back of the card will have spaces for the person to write certain information. These are the categories that can be filled in by hand:
• Name:
• Procedure performed:
• Date of procedure (month/year):
• Treating Clinic Name:
• Treating Clinic Signature:
• Somewhere down the bottom should be something along the lines of:
• supplied from marcuswheelan.com.au
Nice to have
• A nice design with imagery/colours etc ... not just the text on a white background! Bright attractive colours preferred.
• I have uploaded my logo ... a roughly triangular image followed by my name etc. The triangular logo image could be used somewhere on the card and this logo can be interchangeable for other clinics who purchase the card.
• **Please note that I don't want my name to be included as part of the logo on the card ... just use the triangular image on the side of the logo without the following name**
• Also, the colouring of the card does not have to reflect my logo colours as I am anticipating interchanging this logo with other logos if other clinics choose to adopt the card. I am interested to see other, more generic, colour choices as well as my logo colours

```html
<!DOCTYPE html>
<html lang="en">
<head>
<meta charset="utf-8">
<title>Weight Loss Surgery Meal Card</title>
<link rel="stylesheet" href="https://fonts.googleapis.com/css2?family=Roboto+Condensed:wght@300;400;700&display=swap">
<style>
  :root {
    --page: #ffffff;
    --card-bg: #f4f4f4;
    --plate-light: #fbfbfb;
    --plate-mid: #e6e6e6;
    --plate-edge: #d2d2d2;
    --ink-dark: #474747;
    --ink-mid: #5e5e5e;
    --ink-soft: #7a7a7a;
    --ink-faint: #9a9a9a;
    --band: rgba(255,255,255,0.75);
    --band-line: #cfcfcf;
    --bullet-band: #ded3d5;
    --teal: #2a9d8f;
    --food-warm: #e9c089;
    --food-plate: #faf8f4;
    --cutlery: #b9b9b9;
  }
  * { margin: 0; padding: 0; box-sizing: border-box; }
  html, body { width: 1200px; height: 1200px; overflow: hidden; background: var(--page); }
  body { position: relative; font-family: "Roboto Condensed", "Arial Narrow", sans-serif; }

  .card {
    position: absolute;
    left: 181px;
    width: 840px;
    height: 480px;
    overflow: hidden;
    background: var(--card-bg);
    box-shadow: 0 2px 8px rgba(0,0,0,0.18);
  }
  .card--back { top: 110px; }
  .card--front { top: 614px; }

  /* Back: details form */
  .table-scene {
    position: absolute; inset: 0;
    background:
      radial-gradient(circle at 42% 58%, var(--plate-light) 0, var(--plate-mid) 48%, var(--plate-edge) 50%, #ececec 52%, #f6f6f6 75%),
      var(--card-bg);
  }
  .cutlery-knife {
    position: absolute; left: 712px; top: 134px; width: 40px; height: 346px;
    border-radius: 20px 20px 4px 4px;
    background: linear-gradient(90deg, #d9d9d9, var(--cutlery), #e2e2e2);
  }
  .clinic-mark {
    position: absolute; display: flex; align-items: center; gap: 8px;
    color: var(--teal); font-weight: 700; letter-spacing: 0.5px;
  }
  .clinic-mark__dot { width: 14px; height: 14px; border-radius: 50%; background: var(--teal); }
  .card--back .clinic-mark { right: 90px; top: 60px; font-size: 26px; }

  .field {
    position: absolute; left: 120px; width: 560px; height: 50px;
    display: flex; align-items: center;
    background: linear-gradient(90deg, rgba(255,255,255,0) 0, var(--band) 8%, var(--band) 85%, rgba(255,255,255,0));
    border-bottom: 6px solid var(--band-line);
    font-size: 26px; font-weight: 300; color: var(--ink-mid);
  }
  .field::before {
    content: ""; width: 10px; height: 10px; border-radius: 50%;
    background: #fff; box-shadow: 0 0 3px rgba(0,0,0,0.3);
    margin: 0 14px 0 4px;
  }
  .field__slash { margin-left: 60px; }
  .field--name { top: 135px; }
  .field--procedure { top: 199px; }
  .field--date { top: 265px; }
  .field--clinic { top: 329px; }
  .field--signature { top: 394px; }

  .supplier-note {
    position: absolute; left: 795px; top: 450px;
    transform: rotate(-90deg); transform-origin: left top;
    font-size: 14px; font-weight: 300; color: var(--ink-faint); white-space: nowrap;
  }
  .supplier-note strong { font-weight: 400; color: var(--ink-mid); }

  /* Front: message */
  .linen { position: absolute; inset: 0; background: linear-gradient(120deg, #fafafa, #eeeeee 70%, #e8e8e8); }
  .food-photo {
    position: absolute; left: -60px; top: -80px; width: 350px; height: 340px;
    border-radius: 50%;
    background: radial-gradient(circle at 40% 45%, var(--food-warm) 0, #d9a764 28%, var(--food-plate) 55%, var(--food-plate) 96%, #d8b46a 98%);
  }
  .fork-photo {
    position: absolute; left: 766px; top: 230px; width: 40px; height: 250px;
    border-radius: 6px 6px 3px 3px;
    background: linear-gradient(90deg, #d6d6d6, var(--cutlery), #dedede);
  }
  .headline {
    position: absolute; right: 38px; top: 62px; text-align: right;
    font-size: 52px; font-weight: 700; line-height: 48px; letter-spacing: -0.5px;
    color: var(--ink-dark);
  }
  .headline__em { color: var(--ink-soft); }

  .notice {
    position: absolute; left: 163px; width: 612px;
    padding-left: 86px; font-size: 29px; font-weight: 300; line-height: 34px;
    color: var(--ink-mid);
  }
  .notice::before {
    content: ""; position: absolute; left: 64px; top: 12px;
    width: 10px; height: 10px; border-radius: 50%; background: var(--ink-soft);
  }
  .notice strong { font-weight: 700; }
  .notice--limit {
    top: 234px; height: 78px; padding-top: 5px;
    background: linear-gradient(90deg, rgba(222,211,213,0) 0, var(--bullet-band) 18%, var(--bullet-band) 90%, rgba(222,211,213,0));
  }
  .notice--request { top: 318px; color: var(--ink-soft); }
  .notice--request::before { top: 14px; }
  .notice--request strong { color: var(--ink-mid); }
  .notice__example { display: block; font-size: 19px; line-height: 24px; color: var(--ink-mid); }

  .card--front .clinic-mark { left: 48px; top: 360px; font-size: 28px; }
</style>
</head>
<body>

<section class="card card--back" aria-label="Patient details side">
  <div class="table-scene" role="img" aria-label="Photo of an empty white dinner plate on a linen tablecloth"></div>
  <div class="cutlery-knife" role="img" aria-label="Photo of a silver table knife"></div>
  <div class="clinic-mark"><span class="clinic-mark__dot"></span>Wheelan</div>

  <div class="field field--name">Name:</div>
  <div class="field field--procedure">Procedure performed:</div>
  <div class="field field--date">Date of procedure (month/year):<span class="field__slash">/</span></div>
  <div class="field field--clinic">Treating Clinic Name:</div>
  <div class="field field--signature">Treating Clinic Signature:</div>

  <p class="supplier-note">Meal cards available at <strong>marcuswheelan.com.au</strong></p>
</section>

<section class="card card--front" aria-label="Message to restaurant side">
  <div class="linen"></div>
  <div class="food-photo" role="img" aria-label="Photo of a crepe topped with kiwi fruit and blueberries with orange slices on a white plate"></div>
  <div class="fork-photo" role="img" aria-label="Photo of a silver fork"></div>

  <h1 class="headline">the individual bearing<br>this card has undergone<br><span class="headline__em">weight loss surgery</span></h1>

  <p class="notice notice--limit">This surgery restricts portion sizes to<br>between <strong>half and one cup</strong> of food at a time.</p>
  <p class="notice notice--request">Please give consideration to allowing <strong>smaller portions</strong> of your regular meals to be ordered to <strong>reduce wastage</strong> and <strong>excess costs</strong>.
    <span class="notice__example">For example: a half size portion priced at two thirds of usual cost.</span></p>

  <div class="clinic-mark"><span class="clinic-mark__dot"></span>Wheelan</div>
</section>

</body>
</html>
```